Make a website for Velmoro, a Luxury and Modern Concierge Platform based in the UAE

Concierge Platform that has various luxury and exotic actives available to clients, itinerary planning for a dubai / uae based holiday.
Want the website to appear luxury, modern and easy to understand, with a landing page that can captivate customers, majority will use Mobile but Desktop should look good too. Whatsapp Contact pop-out, and email sign up list. Social Link (Facebook, Instagram, Whatsapp, Whatsapp Broadcast, Twitter/X, etc).
Ability to make it Dark and Light themed.
Second page Page that has a list of activities on a drop down/ list, as follows:
Flights
Car Rental
Luxury Car Rental
Chauffer
Yachts/ Boats
Jet Ski / Watersports
Buggies/ ATV
Dining
Tickets/Events
Apartments/ Hotels
Personal Shopping.
Link to competitors, who's websites appear basic and could be 100% improved, for examples:
- https://www.hushedgetaways.example/
- https://www.tavix.example/
- https://www.dubai-latch.example/
- https://thevorlanhouse.example/dubai.html
- https://www.thegildedattendant.example/concierge-service-dubai/
Open to logo designs, we own Velmoro.com.
Colours:
Luxury Style, Black and Gold is often used, but maybe over-used?
A modern colour palette White, Light Blue, Light Grey, but we aren't experts at this, so this isn't by any means strict criteria, let the creative mind run free.
Thank you

```html
<!DOCTYPE html>
<html lang="en">
<head>
<meta charset="utf-8">
<title>Velmoro — Luxury Concierge, UAE</title>
<link rel="stylesheet" href="https://fonts.googleapis.com/css2?family=Bebas+Neue&family=Pathway+Gothic+One&display=swap">
<style>
  :root {
    --cream: #fbf0dc;
    --ink: #0a0703;
    --amber-deep: #2a1a08;
    --amber-mid: #3d2710;
    --rule: #ffffff;
    --gold: #a8864e;
  }
  * { box-sizing: border-box; margin: 0; padding: 0; }
  html, body {
    width: 1200px; height: 596px; overflow: hidden;
    background: var(--ink);
  }
  .hero {
    position: relative;
    width: 1200px; height: 596px;
    overflow: hidden;
    color: var(--cream);
  }
  .hero-backdrop {
    position: absolute; inset: 0;
    background:
      radial-gradient(ellipse 420px 220px at 720px 300px, rgba(120,78,24,.45), transparent 70%),
      radial-gradient(ellipse 300px 200px at 1050px 290px, rgba(110,60,20,.4), transparent 70%),
      radial-gradient(ellipse 260px 260px at 160px 220px, rgba(70,50,25,.45), transparent 70%),
      linear-gradient(180deg, #0d0905 0%, #24180a 40%, var(--amber-deep) 62%, #070502 100%);
  }
  .site-header {
    position: absolute; left: 0; top: 0;
    width: 100%; height: 74px;
    border-bottom: 2px solid var(--rule);
  }
  .brand {
    position: absolute; left: 60px; top: 28px; height: 36px;
    display: flex; align-items: center; gap: 8px;
    font-family: Arial, Helvetica, sans-serif;
    font-weight: 700; font-size: 24px; letter-spacing: .3px;
    color: var(--cream);
  }
  .brand-mark {
    width: 32px; height: 32px; border-radius: 50%;
    border: 2px solid var(--gold);
  }
  .menu-toggle {
    position: absolute; left: 1073px; top: 30px;
    width: 45px; height: 25px;
    display: flex; flex-direction: column; justify-content: space-between;
  }
  .menu-toggle span { display: block; height: 5px; background: var(--cream); }
  .hero-title {
    position: absolute; left: 0; top: 0;
    width: 1200px; height: 596px;
    overflow: visible;
  }
  .hero-title text {
    font-family: "Bebas Neue", "League Gothic", sans-serif;
    font-size: 368px;
    fill: var(--cream);
  }
  .hero-copy {
    position: absolute; left: 915px; top: 342px;
    font-family: "Pathway Gothic One", "Oswald", sans-serif;
    font-size: 18.5px; line-height: 24.4px;
    color: var(--cream);
  }
  .hero-copy span { display: block; white-space: nowrap; }
  .cta {
    position: absolute; left: 915px; top: 516px;
    display: flex; align-items: center; gap: 10px;
    font-family: "Pathway Gothic One", "Oswald", sans-serif;
    font-size: 48px; line-height: 1; white-space: nowrap;
    color: var(--cream); text-decoration: none;
  }
  .cta svg { width: 26px; height: 26px; margin-top: 6px; }
</style>
</head>
<body>
<main class="hero">
  <div class="hero-backdrop" role="img" aria-label="Dimly lit luxury bar interior with warm amber lighting"></div>

  <header class="site-header">
    <div class="brand"><span class="brand-mark"></span>VELMORO</div>
    <div class="menu-toggle" aria-label="Menu"><span></span><span></span><span></span></div>
  </header>

  <svg class="hero-title" viewBox="0 0 1200 596" aria-labelledby="hero-title-text">
    <text id="hero-title-text" x="14" y="514" textLength="847" lengthAdjust="spacingAndGlyphs">VELMORO</text>
  </svg>

  <p class="hero-copy">
    <span>Lorem ipsum dolor, sit amet consectetur</span>
    <span>adipisicing elit. Laudantium autem hic</span>
    <span>dignissimos amet distinctio culpa repellendus</span>
    <span>consequatur blanditiis sint quas, saepe</span>
    <span>consequuntur quidem accusantium debitis et</span>
    <span>nesciunt deleniti eos molestiae!</span>
  </p>

  <a class="cta" href="#contact">Get in touch
    <svg viewBox="0 0 24 24" fill="none" stroke="currentColor" stroke-width="2.6" stroke-linecap="square">
      <path d="M11 4H4v16h16v-7"/>
      <path d="M14 3h7v7"/>
      <path d="M21 3L11 13"/>
    </svg>
  </a>
</main>
</body>
</html>
```